We need a groovy retro poster for a comedy show called Shimmy Starfield :)

Hi there!
- We need a show poster for a comedy show called "Shimmy Starfield" starring Lydia Brenner.
- We want the show to have a retro groovy 60s/70s vibe with bright colors
- We will need some space to add dates and ticket info later.
- Please use 8.5 x 11 for sizing.

Target Market(s)

Men and women 40 and older, GenX

Industry/Entity Type

Entertainment

Requirements
Must have
• Artist Name: Lydia Brenner
Show Name: Shimmy Starfield
Show Description: A Night of Funky Laughs
Nice to have
• - We would like the headshot photo that is uploaded here to be more of a stylized in a cartoon/illustration way so that it is not just a photo.
- Colorful retro graphics.
- We have provided some samples that we like but are open to other ideas.
- We really like the Disco poster sample that is attached to the brief but would need the lady stylized with hair/face like Lydia
- We also like the style and colors of the Twirl Paradise poster attached to the brief but need the face/hair more like Lydia
- The postcard attached to the brief is just to give an example of branding colors that are currently being used. Not necessary to use them but just to give you an idea.
Should not have
• Please no trite references to stand up comedy such as stage and spotlight. A microphone is ok but only if it fits the illustration.

Thanks!

```html
<!DOCTYPE html>
<html lang="en">
<head>
<meta charset="utf-8">
<title>Shimmy Starfield – Lydia Brenner</title>
<link rel="stylesheet" href="https://fonts.googleapis.com/css2?family=Righteous&family=Oswald:wght@400&family=Open+Sans:wght@400;600&display=swap">
<style>
  :root {
    --navy: #1d2358;
    --navy-deep: #161b47;
    --splash: #1f4a8a;
    --orange: #f28a1e;
    --cyan: #5ec8d8;
    --red: #ef4f24;
    --yellow: #f7c95a;
    --white: #ffffff;
    --shadow: rgba(8, 10, 35, 0.55);
  }
  * { margin: 0; padding: 0; box-sizing: border-box; }
  html, body { width: 977px; height: 1200px; overflow: hidden; background: var(--navy); }
  .poster {
    position: relative;
    width: 977px;
    height: 1200px;
    overflow: hidden;
    background: radial-gradient(ellipse at 45% 35%, #222a66 0%, var(--navy) 55%, var(--navy-deep) 100%);
    font-family: "Open Sans", sans-serif;
    color: var(--white);
  }
  .headshot {
    position: absolute;
    left: 94px; top: 30px;
    width: 540px; height: 600px;
    border-radius: 46% 40% 8% 12% / 40% 36% 6% 8%;
    background:
      radial-gradient(ellipse 35% 30% at 50% 30%, #e8d9b8 0%, #d8c298 60%, transparent 100%),
      radial-gradient(ellipse 60% 50% at 50% 85%, #1f5d78 0%, #1b4b6a 70%, transparent 100%),
      radial-gradient(ellipse at 50% 45%, var(--splash) 0%, rgba(31,74,138,0.4) 70%, transparent 100%);
  }
  .star { position: absolute; }
  .burst { position: absolute; left: 680px; top: 170px; width: 230px; height: 190px; }
  .name-badge {
    position: absolute;
    left: 510px; top: 285px;
    width: 395px; height: 385px;
    border-radius: 50%;
    background: var(--orange);
    display: flex; flex-direction: column; align-items: center; justify-content: center;
    font-family: "Righteous", sans-serif;
    text-transform: uppercase;
    line-height: 1;
  }
  .name-badge .first { font-size: 46px; letter-spacing: 1px; }
  .name-badge .last { font-size: 70px; letter-spacing: 1px; margin-top: 4px; }
  .tagline {
    position: absolute;
    left: 200px; top: 572px;
    width: 690px; height: 100px;
    transform: rotate(-4deg);
  }
  .tagline svg { position: absolute; inset: 0; }
  .tagline span {
    position: absolute; inset: 0;
    display: flex; align-items: center; justify-content: center;
    font-family: "Oswald", sans-serif;
    font-size: 40px; letter-spacing: 1px;
    text-transform: uppercase;
    padding-left: 30px;
  }
  .rule { position: absolute; left: 220px; top: 700px; }
  .title {
    position: absolute;
    left: 0; width: 977px;
    text-align: center;
    font-family: "Righteous", sans-serif;
    line-height: 1;
  }
  .title-main {
    top: 722px;
    font-size: 200px;
    letter-spacing: 4px;
    color: var(--orange);
    background: repeating-linear-gradient(90deg, var(--orange) 0 62px, var(--cyan) 62px 124px);
    -webkit-background-clip: text;
    background-clip: text;
    -webkit-text-fill-color: transparent;
    -webkit-text-stroke: 3px var(--white);
    filter: drop-shadow(6px 8px 4px var(--shadow));
  }
  .title-sub {
    top: 895px;
    font-size: 118px;
    letter-spacing: 3px;
    color: var(--white);
    text-shadow: 3px 0 0 var(--cyan), 6px 8px 6px var(--shadow);
  }
  .date-ribbon {
    position: absolute;
    left: 140px; top: 1045px;
    width: 740px; height: 78px;
  }
  .date-ribbon svg { position: absolute; inset: 0; }
  .date-ribbon span {
    position: absolute; inset: 0;
    display: flex; align-items: center; justify-content: center;
    font-size: 40px; letter-spacing: 1px; text-transform: uppercase;
  }
  .contact {
    position: absolute;
    left: 0; top: 1152px; width: 977px;
    text-align: center;
    font-size: 19px;
  }
  .contact .sep { margin: 0 12px; }
</style>
</head>
<body>
<main class="poster">
  <div class="headshot" role="img" aria-label="Stylized portrait of Lydia Brenner, smiling, blonde hair, teal zip top, over a blue paint splash"></div>

  <svg class="star" style="left:150px;top:240px" width="48" height="48" viewBox="0 0 24 24"><polygon fill="var(--cyan)" points="12,1 15,9 23,9 16.5,14 19,22 12,17 5,22 7.5,14 1,9 9,9"/></svg>
  <svg class="star" style="left:845px;top:700px" width="78" height="78" viewBox="0 0 24 24"><polygon fill="var(--cyan)" points="12,1 15,9 23,9 16.5,14 19,22 12,17 5,22 7.5,14 1,9 9,9"/></svg>
  <svg class="star" style="left:880px;top:820px" width="22" height="22" viewBox="0 0 24 24"><polygon fill="var(--yellow)" points="12,1 15,9 23,9 16.5,14 19,22 12,17 5,22 7.5,14 1,9 9,9"/></svg>
  <svg class="star" style="left:760px;top:700px" width="14" height="14" viewBox="0 0 24 24"><polygon fill="var(--yellow)" points="12,1 15,9 23,9 16.5,14 19,22 12,17 5,22 7.5,14 1,9 9,9"/></svg>

  <svg class="burst" viewBox="0 0 230 190" role="img" aria-label="Retro illustration of a horn with a yellow burst">
    <polygon fill="var(--yellow)" points="115,10 135,60 190,35 165,85 225,100 165,120 185,175 130,140 100,185 95,135 35,160 65,110 5,90 70,75 45,25 100,55"/>
  </svg>

  <div class="name-badge">
    <span class="first">Lydia</span>
    <span class="last">Brenner</span>
  </div>

  <div class="tagline">
    <svg viewBox="0 0 690 100" preserveAspectRatio="none"><polygon fill="var(--cyan)" points="0,8 690,0 670,100 20,92"/></svg>
    <span>A Night of Funky Laughs</span>
  </div>

  <svg class="rule" width="660" height="14" viewBox="0 0 660 14">
    <rect x="0" y="4" width="40" height="6" rx="3" fill="var(--cyan)"/>
    <rect x="52" y="4" width="560" height="6" rx="3" fill="var(--cyan)"/>
    <rect x="624" y="4" width="30" height="6" rx="3" fill="var(--cyan)"/>
  </svg>

  <h1 class="title title-main">Shimmy</h1>
  <h2 class="title title-sub">Starfield</h2>

  <div class="date-ribbon">
    <svg viewBox="0 0 740 78" preserveAspectRatio="none"><polygon fill="var(--red)" points="0,0 740,0 715,39 740,78 0,78 25,39"/></svg>
    <span>Saturday, August 18th</span>
  </div>

  <p class="contact">Contact &amp; Booking: Hal Denton Entertainment<span class="sep">•</span>hal@haldenton.com<span class="sep">•</span>555-014-2290</p>
</main>
</body>
</html>
```